Contemporary Media Company with Logo Needs Business Card Design

Need a modern card design for a full service digital media company using the logo included. Also want the info below on the card. Probably list the services on the card back to save space for the front. Want something contemporary to impress prospective clients. You may want to submit both a somewhat more conservative design, and then a more wild one.
General Info: (this phrase need not be on the card)
Tod Parvin
Founder and CEO
949-628-4513
tod@lumavantstudio.example
lumavantstudio.example
Services: (this word need not be on the card)
Content & Experience Strategy
Brand Development
Search Engine Optimization
Website Design
Website Operation
Social Media Integration
Complete Video Solutions
Industry/Entity Type
Business
Contact Information for Business Card
Tod Parvin
Founder and CEO
949-628-4513
tod@lumavantstudio.example
lumavantstudio.example
Brand Development
Website Design
Website Operation
Social Media Integration
Complete Video Solutions
Look and feel

```html
<!DOCTYPE html>
<html lang="en">
<head>
<meta charset="utf-8">
<title>Lumavant Studio — Business Card</title>
<link rel="stylesheet" href="https://fonts.googleapis.com/css2?family=Montserrat:wght@500&family=Open+Sans:wght@300;400;600&display=swap">
<style>
  :root {
    --bg: #e4e2df;
    --paper: #ffffff;
    --paper-shade: #f3f3f3;
    --slate: #5e5f61;
    --slate-text: #6a6b6d;
    --ink: #2f3033;
    --orange: #ee7d22;
    --on-slate: #f2f2f2;
  }
  * { margin: 0; padding: 0; box-sizing: border-box; }
  html, body { width: 1200px; height: 902px; overflow: hidden; }
  body {
    background: var(--bg);
    font-family: "Open Sans", Arial, sans-serif;
    display: flex;
    flex-direction: column;
    align-items: center;
    justify-content: center;
    gap: 40px;
  }
  .card {
    position: relative;
    width: 700px;
    height: 400px;
    background: linear-gradient(160deg, var(--paper) 60%, var(--paper-shade));
    box-shadow: 0 6px 18px rgba(0,0,0,0.18);
    overflow: hidden;
  }

  /* Back side */
  .services {
    position: absolute;
    top: 46px;
    right: 52px;
    list-style: none;
    text-align: right;
    color: var(--ink);
    font-size: 22px;
    font-weight: 600;
    line-height: 1.32;
  }
  .services li::after {
    content: "";
    display: inline-block;
    width: 9px;
    height: 9px;
    margin-left: 12px;
    vertical-align: middle;
    background: var(--orange);
    border-radius: 50%;
  }

  /* Front side */
  .front .wave { position: absolute; inset: 0; }
  .brand {
    position: absolute;
    top: 84px;
    left: 96px;
    display: flex;
    align-items: center;
    gap: 16px;
    white-space: nowrap;
  }
  .brand-square {
    width: 34px;
    height: 34px;
    background: var(--orange);
  }
  .brand-name {
    font-family: "Montserrat", "Open Sans", sans-serif;
    font-weight: 500;
    font-size: 40px;
    line-height: 1;
    letter-spacing: 2px;
    color: var(--slate-text);
    text-transform: uppercase;
  }
  .person {
    position: absolute;
    left: 175px;
    top: 290px;
    width: 170px;
    text-align: right;
    color: var(--on-slate);
    font-weight: 300;
  }
  .person-name { font-size: 27px; line-height: 1.2; }
  .person-title { font-size: 17px; line-height: 1.3; white-space: nowrap; }
  .divider {
    position: absolute;
    left: 368px;
    top: 238px;
    width: 2px;
    height: 120px;
    background: var(--on-slate);
  }
  .contacts {
    position: absolute;
    left: 390px;
    top: 236px;
    list-style: none;
    color: var(--on-slate);
    font-size: 18px;
    font-weight: 300;
    line-height: 1.5;
    white-space: nowrap;
  }
  .contacts li { display: flex; align-items: center; gap: 8px; }
  .contacts svg { width: 18px; height: 18px; flex: none; }
</style>
</head>
<body>

  <section class="card back" aria-label="Card back">
    <ul class="services">
      <li>Website Design</li>
      <li>Website Operation</li>
      <li>Brand Development</li>
      <li>Social Media Integration</li>
      <li>Complete Video Solutions</li>
    </ul>
  </section>

  <section class="card front" aria-label="Card front">
    <svg class="wave" viewBox="0 0 700 400" preserveAspectRatio="none" aria-hidden="true">
      <path d="M0,312 C170,300 270,214 400,200 C520,188 610,150 700,108 L700,400 L0,400 Z" fill="var(--orange)"/>
      <path d="M0,324 C170,312 270,226 400,212 C520,200 610,162 700,120 L700,400 L0,400 Z" fill="var(--slate)"/>
    </svg>

    <div class="brand">
      <span class="brand-square"></span>
      <span class="brand-name">Lumavant Studio</span>
    </div>

    <div class="person">
      <p class="person-name">Tod Parvin</p>
      <p class="person-title">Founder and CEO</p>
    </div>

    <span class="divider"></span>

    <ul class="contacts">
      <li>
        <svg viewBox="0 0 18 18" aria-hidden="true"><rect width="18" height="18" rx="2" fill="var(--on-slate)"/><path d="M5 4c1 0 2 2 2 3s-1 1-1 2 2 3 3 3 1-1 2-1 3 1 3 2-1 2-2 2C8 15 3 10 3 6c0-1 1-2 2-2z" fill="var(--slate)"/></svg>
        949-628-4513
      </li>
      <li>
        <svg viewBox="0 0 18 18" aria-hidden="true"><rect width="18" height="18" rx="2" fill="var(--on-slate)"/><rect x="3" y="5" width="12" height="8" fill="none" stroke="var(--slate)" stroke-width="1.4"/><path d="M3 5l6 5 6-5" fill="none" stroke="var(--slate)" stroke-width="1.4"/></svg>
        tod@lumavantstudio.example
      </li>
      <li>
        <svg viewBox="0 0 18 18" aria-hidden="true"><rect width="18" height="18" rx="2" fill="var(--on-slate)"/><circle cx="9" cy="9" r="5.5" fill="none" stroke="var(--slate)" stroke-width="1.4"/><path d="M3.5 9h11M9 3.5c-2.5 3-2.5 8 0 11M9 3.5c2.5 3 2.5 8 0 11" fill="none" stroke="var(--slate)" stroke-width="1.1"/></svg>
        lumavantstudio.example
      </li>
    </ul>
  </section>

</body>
</html>
```